Brambury Logistics

Create a modern, simple, Elegant business card design for my business.

Services: Tamo Trucks, Transport, Contract Logistics,

Industry/Entity Type

Business

Contact Information for Business Card

Include all details same as old card plus new website address: www.bramburylogistics.com.au

Requirements
Must have
• Similar colors to Logo.

```html
<!DOCTYPE html>
<html lang="en">
<head>
<meta charset="utf-8">
<title>Brambury Logistics – Business Card</title>
<link rel="stylesheet" href="https://fonts.googleapis.com/css2?family=Source+Sans+3:wght@400;600;700&display=swap">
<style>
  :root {
    --backdrop: #161616;
    --card-front: #f4f4f4;
    --brand-blue: #1a6aa8;
    --brand-grey: #7a7a7a;
    --text-grey: #5c5c5c;
    --back-top: #0aa6de;
    --back-bottom: #02568a;
    --white: #ffffff;
  }
  * { margin: 0; padding: 0; box-sizing: border-box; }
  html, body {
    width: 1200px; height: 900px; overflow: hidden;
    background: var(--backdrop);
    font-family: "Source Sans 3", "Myriad Pro", sans-serif;
  }
  .card {
    position: absolute;
    top: 184px;
    width: 302px; height: 490px;
    border-radius: 12px;
  }
  .card-front {
    left: 298px;
    background: var(--card-front);
    color: var(--text-grey);
    text-align: center;
  }
  .card-back {
    left: 646px;
    background: linear-gradient(180deg, var(--back-top) 0%, var(--back-bottom) 100%);
  }
  .brand-name {
    position: absolute;
    left: 0; right: 0; top: 112px;
    font-size: 27px; font-weight: 700;
    color: var(--brand-grey);
    letter-spacing: 0.2px;
  }
  .person-name {
    position: absolute; left: 0; right: 0; top: 212px;
    font-size: 17px; font-weight: 600; color: var(--brand-blue);
  }
  .person-role {
    position: absolute; left: 0; right: 0; top: 233px;
    font-size: 14px;
  }
  .contact {
    position: absolute; left: 0; right: 0; top: 285px;
    font-size: 14px; line-height: 18px;
  }
  .address {
    position: absolute; left: 0; right: 0; top: 352px;
    font-size: 14px; line-height: 18px;
  }
  .back-brand {
    position: absolute;
    left: 50%; top: 50%;
    transform: translate(-50%, -50%) rotate(-90deg);
    white-space: nowrap;
    font-size: 40px; font-weight: 700;
    color: var(--white);
  }
</style>
</head>
<body>
  <section class="card card-front">
    <div class="brand-name">Brambury Logistics</div>
    <div class="person-name">Daniel Hartley</div>
    <div class="person-role">Managing Director</div>
    <div class="contact">
      044-987 654 321<br>
      info@brambury.com.au<br>
      www.bramburylogistics.com.au
    </div>
    <div class="address">
      12345, Address Goes Here Country<br>
      Name, 123456.
    </div>
  </section>
  <section class="card card-back">
    <div class="back-brand">Brambury Logistics</div>
  </section>
</body>
</html>
```